Modern 6 page design, business card, and a banner

I need a website design for my CFO service. The service uses proprietary tech, so it needs to be modern. I also need business card and banner design to match the site.
The banner size is 33.75 X 79.25.
I'm open to colors and styles.

Target Market(s)

Startups

Coding

Coded - Design and coding required

Number of Pages Required

5+ page

```html
<!DOCTYPE html>
<html lang="en">
<head>
<meta charset="utf-8">
<title>Tallo — Strategic Financial Planner</title>
<link href="https://fonts.googleapis.com/css2?family=Varela+Round&family=Open+Sans:ital,wght@0,300;0,400;0,600;0,700;1,700&display=swap" rel="stylesheet">
<style>
:root{
  --blue:#2f6db5;
  --blue-dark:#245a98;
  --rose:#c27a70;
  --ink:#1b1f24;
  --ink-2:#232830;
  --text:#3c3f44;
  --line:#dde6ef;
  --white:#ffffff;
}
*{box-sizing:border-box;margin:0;padding:0}
html,body{width:1200px;height:4724px;overflow:hidden}
body{position:relative;background:var(--white);font-family:"Open Sans",sans-serif;color:var(--text)}
.abs{position:absolute}
svg{display:block}

/* hero */
.hero{left:0;top:0;width:1200px;height:800px;background:linear-gradient(160deg,#4a525e 0%,#2c323b 45%,#1d2229 100%)}
.hero-contact{top:30px;left:712px;display:flex;gap:26px;font-size:11px;color:#fff;font-weight:600}
.hero-contact span{display:flex;align-items:center;gap:8px}
.main-nav{top:77px;left:352px;display:flex;gap:32px;font-size:11px;font-weight:700;color:#fff;letter-spacing:.3px}
.hero-logo{top:238px;left:0;width:1200px;text-align:center;font-weight:300;font-size:150px;line-height:1;color:#fff;letter-spacing:4px}
.hero-tag{top:468px;left:0;width:1200px;text-align:center;font-size:24px;font-weight:300;color:var(--rose);letter-spacing:.5px}

/* section titles */
.section-title{font-family:"Varela Round",sans-serif;color:var(--blue);font-size:50px;text-align:center}
.divider{width:164px;height:14px}

/* how it works */
.step{background:#fff;border-right:3px solid var(--line);border-bottom:3px solid var(--line);padding:22px 8px 0 10px}
.step.accent{border-color:var(--rose)}
.step-head{display:flex;align-items:center;gap:6px;margin-bottom:22px}
.step-head h3{font-family:"Open Sans",sans-serif;font-weight:400;font-size:27px;color:var(--ink);border-bottom:2px solid var(--blue);line-height:1.25}
.step p{font-size:16px;line-height:29px;color:var(--text)}

/* services */
.dark{left:0;top:1600px;width:1200px;height:1380px;background:var(--ink)}
.service{border:1.5px solid var(--blue);text-align:center;color:#fff;padding:70px 28px 0}
.service.filled{background:var(--blue)}
.service h3{font-size:24px;font-weight:700;line-height:35px;margin-bottom:16px}
.service p{font-size:13.5px;line-height:25px}
.hex{top:-50px;left:50%;margin-left:-52px;width:104px;height:96px}
.see-more{bottom:-2px;left:50%;margin-left:-58px;width:116px;height:24px;background:#fff;border-radius:12px 12px 0 0;font-size:12px;color:var(--blue);line-height:24px;font-weight:600}

/* mobile developing */
.photo{border-radius:6px}
.feature h3{font-family:"Open Sans",sans-serif;font-weight:600;font-size:23px;line-height:32px;color:var(--rose);margin-bottom:14px}
.feature p{font-size:13.5px;line-height:25.5px;color:var(--ink)}
.pill-btn{background:#fff;color:var(--rose);font-size:15px;font-weight:700;border-radius:18px;padding:6px 22px;display:flex;align-items:center;gap:10px}

/* footer */
.footer{left:0;top:4100px;width:1200px;height:624px;background:radial-gradient(ellipse at 70% 40%,#23303a 0%,#141a20 60%,#0f1418 100%)}
.quote-title{top:4268px;left:0;width:1200px;text-align:center;color:#fff;font-size:30px;font-weight:700}
.quote-title em{font-style:italic}
.field{height:38px;border:1.5px solid var(--rose);border-radius:19px;color:#d8d8d8;font-size:13px;line-height:35px;padding-left:18px}
.submit{top:4402px;left:748px;width:118px;height:38px;border-radius:19px;background:var(--rose);color:#fff;font-size:14px;display:flex;align-items:center;justify-content:center;gap:10px}
.foot-logo{top:4506px;left:0;width:1200px;text-align:center;font-weight:300;font-size:92px;line-height:1;color:#fff;letter-spacing:3px}
.foot-nav{top:4633px;left:0;width:1200px;display:flex;justify-content:center;gap:34px;font-size:11.5px;color:#fff}
.copyright{top:4676px;left:0;width:1200px;text-align:center;font-size:11px;color:#fff;letter-spacing:.3px}
</style>
</head>
<body>

<!-- Hero -->
<div class="abs hero" role="img" aria-label="Photo of a financial advisor in a suit explaining a plan to a client across a meeting table"></div>
<div class="abs hero-contact">
  <span><svg width="14" height="14" viewBox="0 0 24 24"><path fill="#2f6db5" d="M6.6 10.8a15 15 0 0 0 6.6 6.6l2.2-2.2c.3-.3.7-.4 1-.2 1.1.4 2.3.6 3.6.6.6 0 1 .4 1 1V20c0 .6-.4 1-1 1A17 17 0 0 1 3 4c0-.6.4-1 1-1h3.5c.6 0 1 .4 1 1 0 1.3.2 2.5.6 3.6.1.3 0 .7-.2 1z"/></svg>555-014-2280</span>
  <span><svg width="18" height="13" viewBox="0 0 18 13"><rect width="18" height="13" rx="1.5" fill="#2f6db5"/><path d="M1 1l8 6 8-6" stroke="#1d2229" stroke-width="1.3" fill="none"/></svg>hello@tallofinance.com</span>
</div>
<nav class="abs main-nav"><span>HOME</span><span>HOW IT WORKS</span><span>SERVICE</span><span>MOBILE DEVLOPING</span><span>CONTACT</span></nav>
<div class="abs hero-logo">Tallo</div>
<div class="abs hero-tag">Strategic Financial Planner</div>
<svg class="abs" style="left:0;top:660px" width="1200" height="150" viewBox="0 0 1200 150">
  <polygon points="0,75 342,12 1200,85 1200,150 0,150" fill="#2f6db5"/>
  <polygon points="0,88 342,28 1200,125 1200,150 0,150" fill="#fff"/>
</svg>

<!-- How it works -->
<h2 class="abs section-title" style="left:230px;top:930px;width:360px">How it Works</h2>
<svg class="abs divider" style="left:330px;top:998px" viewBox="0 0 164 14"><line x1="0" y1="7" x2="164" y2="7" stroke="#c27a70" stroke-width="3"/><circle cx="70" cy="7" r="5" fill="#c27a70"/><circle cx="82" cy="7" r="5" fill="#c27a70"/><circle cx="94" cy="7" r="5" fill="#c27a70"/></svg>

<div class="abs step" style="left:645px;top:838px;width:335px;height:204px">
  <div class="step-head"><svg width="56" height="50" viewBox="0 0 56 50"><path fill="#2f6db5" d="M8 8h12a6 6 0 1 1 10 0h10v12a6 6 0 1 1 0 10v10H30a6 6 0 1 0-10 0H8V28a6 6 0 1 0 0-10z"/></svg><h3>Develop Plan</h3></div>
  <p>we work with you to develop a 3 to 5 year financial plan tailored to your business goals.</p>
</div>
<div class="abs step" style="left:220px;top:1088px;width:335px;height:206px">
  <div class="step-head"><svg width="62" height="46" viewBox="0 0 62 46"><rect x="2" y="4" width="46" height="34" fill="none" stroke="#2f6db5" stroke-width="4"/><rect x="10" y="22" width="5" height="10" fill="#2f6db5"/><rect x="18" y="16" width="5" height="16" fill="#2f6db5"/><rect x="26" y="20" width="5" height="12" fill="#2f6db5"/><circle cx="44" cy="20" r="9" fill="#fff" stroke="#2f6db5" stroke-width="4"/><line x1="50" y1="27" x2="58" y2="35" stroke="#2f6db5" stroke-width="5"/><line x1="2" y1="44" x2="48" y2="44" stroke="#2f6db5" stroke-width="3"/></svg><h3>Clean Data</h3></div>
  <p>our bookkeepers clean your historical data, set-up live data intake, and ensure alignment with finance reports.</p>
</div>
<div class="abs step accent" style="left:642px;top:1088px;width:340px;height:206px">
  <div class="step-head"><svg width="56" height="50" viewBox="0 0 56 50"><polygon points="28,2 52,25 28,48 4,25" fill="none" stroke="#2f6db5" stroke-width="3"/><rect x="18" y="14" width="4" height="14" fill="#2f6db5"/><rect x="25" y="10" width="4" height="18" fill="#2f6db5"/><rect x="32" y="16" width="4" height="12" fill="#2f6db5"/><circle cx="28" cy="36" r="7" fill="none" stroke="#2f6db5" stroke-width="3"/></svg><h3>Visual Finances</h3></div>
  <p>we launch your customized visual finance dashboard on Tallo Mobile.</p>
</div>
<div class="abs step" style="left:220px;top:1355px;width:335px;height:208px">
  <div class="step-head"><svg width="56" height="50" viewBox="0 0 56 50"><circle cx="24" cy="28" r="18" fill="none" stroke="#2f6db5" stroke-width="4"/><circle cx="24" cy="28" r="9" fill="none" stroke="#2f6db5" stroke-width="4"/><circle cx="24" cy="28" r="3" fill="#2f6db5"/><line x1="24" y1="28" x2="46" y2="6" stroke="#2f6db5" stroke-width="4"/><polygon points="42,2 52,2 52,12" fill="#2f6db5"/></svg><h3>Monitor Daily</h3></div>
  <p>you monitor real financial results against plan on a daily basis.</p>
</div>
<div class="abs step" style="left:645px;top:1355px;width:335px;height:208px">
  <div class="step-head"><svg width="56" height="54" viewBox="0 0 56 54"><path fill="#2f6db5" d="M10 50V34C4 30 4 18 10 10S30 0 36 8s4 12 4 14l5 8h-5v8c0 3-2 5-5 5h-5v7z"/><line x1="46" y1="14" x2="54" y2="14" stroke="#2f6db5" stroke-width="3"/><line x1="46" y1="22" x2="54" y2="22" stroke="#2f6db5" stroke-width="3"/></svg><h3>Advise Monthly</h3></div>
  <p>our financial experts provide support and help respond as your business grows.</p>
</div>

<!-- Our Service -->
<div class="abs dark"></div>
<svg class="abs" style="left:0;top:1595px" width="1200" height="200" viewBox="0 0 1200 200">
  <polygon points="0,0 1200,0 1200,45 853,181 0,70" fill="#2f6db5"/>
  <polygon points="0,0 1200,0 1200,30 853,160 0,25" fill="#fff"/>
</svg>
<h2 class="abs section-title" style="left:0;top:1855px;width:1200px">Our Service</h2>
<svg class="abs divider" style="left:518px;top:1925px" viewBox="0 0 164 14"><line x1="0" y1="7" x2="164" y2="7" stroke="#c27a70" stroke-width="3"/><circle cx="70" cy="7" r="5" fill="#c27a70"/><circle cx="82" cy="7" r="5" fill="#c27a70"/><circle cx="94" cy="7" r="5" fill="#c27a70"/></svg>

<div class="abs service" style="left:222px;top:2053px;width:346px;height:283px">
  <svg class="abs hex" viewBox="0 0 104 96"><polygon points="26,2 78,2 102,48 78,94 26,94 2,48" fill="#fff"/><rect x="38" y="30" width="28" height="36" fill="none" stroke="#2f6db5" stroke-width="3"/><line x1="44" y1="40" x2="60" y2="40" stroke="#2f6db5" stroke-width="3"/><line x1="44" y1="48" x2="60" y2="48" stroke="#2f6db5" stroke-width="3"/><line x1="44" y1="56" x2="60" y2="56" stroke="#2f6db5" stroke-width="3"/></svg>
  <h3>Plan Development &amp; Accountability</h3>
  <p>We work with every client to develop a tailored 3 to 5 year financial plan and clear measurements to keep them on track...</p>
  <div class="abs see-more">See More</div>
</div>
<div class="abs service filled" style="left:630px;top:2053px;width:348px;height:283px">
  <svg class="abs hex" viewBox="0 0 104 96"><polygon points="26,2 78,2 102,48 78,94 26,94 2,48" fill="#fff"/><circle cx="52" cy="44" r="14" fill="none" stroke="#2f6db5" stroke-width="3"/><circle cx="52" cy="44" r="5" fill="#2f6db5"/><line x1="52" y1="58" x2="52" y2="68" stroke="#2f6db5" stroke-width="3"/></svg>
  <h3>Debt Management</h3>
  <p>Debt is a common financial challenge for businesses of all sizes, and small businesses are no exception...</p>
  <div class="abs see-more">See More</div>
</div>
<div class="abs service" style="left:222px;top:2448px;width:346px;height:282px">
  <svg class="abs hex" viewBox="0 0 104 96"><polygon points="26,2 78,2 102,48 78,94 26,94 2,48" fill="#fff"/><rect x="34" y="38" width="36" height="24" fill="none" stroke="#2f6db5" stroke-width="3"/><circle cx="52" cy="50" r="6" fill="#2f6db5"/><line x1="38" y1="32" x2="66" y2="32" stroke="#2f6db5" stroke-width="3"/></svg>
  <h3>Cash Reserve Plans</h3>
  <p>Being ready for the next opportunity or the next rainy day depends on having the resources on hand totake action...</p>
  <div class="abs see-more">See More</div>
</div>
<div class="abs service" style="left:630px;top:2448px;width:348px;height:282px">
  <svg class="abs hex" viewBox="0 0 104 96"><polygon points="26,2 78,2 102,48 78,94 26,94 2,48" fill="#fff"/><path d="M40 36h18v12c0 8-9 14-9 14s-9-6-9-14z" fill="none" stroke="#2f6db5" stroke-width="3"/><line x1="64" y1="30" x2="64" y2="66" stroke="#2f6db5" stroke-width="3"/><line x1="60" y1="30" x2="70" y2="30" stroke="#2f6db5" stroke-width="3"/></svg>
  <h3>Retirement &amp;<br>Exit Strategies</h3>
  <p>At some point every business owner wonders what the next step will be, whether that's a payoff foryears of hard work..</p>
  <div class="abs see-more">See More</div>
</div>

<svg class="abs" style="left:0;top:2800px" width="1200" height="190" viewBox="0 0 1200 190">
  <polygon points="0,150 343,12 1200,100 1200,190 0,190" fill="#2f6db5"/>
  <polygon points="0,164 343,40 1200,118 1200,190 0,190" fill="#fff"/>
</svg>

<!-- Mobile Developing -->
<h2 class="abs section-title" style="left:0;top:2975px;width:1200px">Mobile Developing</h2>
<svg class="abs divider" style="left:518px;top:3044px" viewBox="0 0 164 14"><line x1="0" y1="7" x2="164" y2="7" stroke="#c27a70" stroke-width="3"/><circle cx="70" cy="7" r="5" fill="#c27a70"/><circle cx="82" cy="7" r="5" fill="#c27a70"/><circle cx="94" cy="7" r="5" fill="#c27a70"/></svg>

<div class="abs photo" style="left:222px;top:3085px;width:335px;height:300px;background:linear-gradient(160deg,#e9ecef 0%,#c9cfd6 60%,#8c939c 100%)" role="img" aria-label="Photo of two colleagues bumping fists over a desk with a monitor and sticky notes"></div>
<div class="abs photo" style="left:642px;top:3085px;width:337px;height:300px;background:linear-gradient(160deg,#5b6a7a 0%,#2f3a47 55%,#1b232c 100%)" role="img" aria-label="Photo of a hand holding a floating transparent dashboard interface"></div>
<div class="abs feature" style="left:218px;top:3408px;width:340px">
  <h3>Real Numbers You<br>Can Trust</h3>
  <p>Any dashboard is only as good as the data it uses. Unlike typical "do-it-yourself" dashboards, our bookkeeping team works directly with your accounting data...</p>
</div>
<div class="abs feature" style="left:640px;top:3408px;width:340px">
  <h3>Always Know Where You<br>Stand</h3>
  <p>Most "outsourced CFO" services are based on last period's financial statements, spreadsheet reportingand built-in lag time for them to catch-up during busy month-end rushes...</p>
</div>

<div class="abs photo" style="left:222px;top:3628px;width:335px;height:302px;background:linear-gradient(160deg,#2c333b 0%,#5f6670 50%,#c7b7a6 100%)" role="img" aria-label="Photo of a developer typing on a laptop beside a monitor full of code"></div>
<div class="abs photo" style="left:642px;top:3628px;width:337px;height:302px;background:linear-gradient(180deg,#d9d3d0 0%,#d2a49a 55%,#c27a70 100%)" role="img" aria-label="Photo of a man reviewing financial statements, tinted rose"></div>
<div class="abs pill-btn" style="left:743px;top:3763px">See More
  <svg width="18" height="10" viewBox="0 0 18 10"><line x1="0" y1="5" x2="15" y2="5" stroke="#c27a70" stroke-width="2"/><polyline points="11,1 16,5 11,9" fill="none" stroke="#c27a70" stroke-width="2"/></svg></div>
<div class="abs feature" style="left:218px;top:3952px;width:340px">
  <h3>Monitoring &amp; Alerts</h3>
  <p>Tallo allows you to monitor your results on a daily basis and measure your progress against both short-term and long-term goalswe also custom-ize alerts based on your goals to help keep you on track and let...</p>
</div>
<div class="abs feature" style="left:640px;top:3952px;width:340px">
  <h3>Backed By Real CFO Services</h3>
  <p>Tallo makes it easy for you to visualize and monitor your company finances and is leading the way in the delivery of customized mobile financial statements. But what really sets us ...</p>
</div>

<!-- Footer -->
<div class="abs footer" role="img" aria-label="Dark background photo of a smartphone showing financial charts"></div>
<svg class="abs" style="left:0;top:4095px" width="1200" height="120" viewBox="0 0 1200 120">
  <polygon points="0,0 1200,0 1200,50 340,112 0,30" fill="#2f6db5"/>
  <polygon points="0,0 1200,0 1200,32 340,96 0,24" fill="#fff"/>
</svg>
<div class="abs quote-title">Request for <em>quote</em></div>
<div class="abs field" style="left:222px;top:4340px;width:360px">Your Name</div>
<div class="abs field" style="left:618px;top:4340px;width:362px">Your Phone</div>
<div class="abs field" style="left:222px;top:4402px;width:360px">Your Email</div>
<div class="abs submit">Submit
  <svg width="16" height="10" viewBox="0 0 16 10"><line x1="0" y1="5" x2="13" y2="5" stroke="#fff" stroke-width="2"/><polyline points="9,1 14,5 9,9" fill="none" stroke="#fff" stroke-width="2"/></svg></div>
<div class="abs foot-logo">Tallo</div>
<nav class="abs foot-nav"><span>HOME</span><span>|</span><span>HOW IT WORKS</span><span>|</span><span>SERVICE</span><span>|</span><span>MOBILE DEVLOPING</span><span>|</span><span>CONTACT</span></nav>
<div class="abs copyright">2019 © All rights reserved by Tallo</div>

</body>
</html>
```